Business Card Design for a Technology Development Company

******* PLEASE NOTE (ALL DESIGNERS): I am going to finish the competition on Monday the 9th July (NOT SATURDAY 15TH). I have some designs I like and need to get them printed next week. Please submit any designs today or tomorrow. *******

PLEASE READ ALL OF THE REQUIREMENTS!!! I've rejected lot's of designs in the past because they didn't read the basic requirements - thanks and good luck!

Quill Harbor is a UK technology / small holding company that invests in startups and develops new ideas. In addition it provides IT Professional Services.

Ideally the design will be simple, professional, smart, and sophisticated, and overall be nice to look at. You can be creative as you like with the design, equally as simple as you like - you guys are the professionals so I'll leave it to your inspiration (make sure you incorporate the logo)!
Updates

PLEASE NOTE (ALL DESIGNERS): I am going to finish the competition on Monday the 9th July (NOT SATURDAY 15TH).  I have some designs I like and need to get them printed next week.  Please submit any designs today or tomorrow.

Target Market(s)

Enterprises / corporations / public sector / technical engineers / investors. More www.brontavex.com / www.pelmora.com than www.flinkaro.com!

Industry/Entity Type

Business

Requirements
Must have
• It should be modern and any artwork (if used) should be simple
- Pastel colours, dark and light colours, and shades are preferred over bright colours
- The design should incorporate the attached Quill Harbor logo and the logo colour scheme
- The logo should be on both sides. The back should just have the logo, maybe with some additional graphics
- It must have the following information on:

FirstName SecondName
Company Position
Email: name@quillharbor.co.uk
Mobile: +44 (0) 7700 900482

- The final design should be for a UK business card, dimensions: 85mm × 55mm
- The final design should have bleed marks to allow for printing and should be given in vector formats (EPS and AI)
Nice to have
• The Logo can be separated from the font in the logo on the front of the card. This isn't necessary or required, just to know it's not a limitation.
Should not have
• No bright colours (I prefer pastel colours, dark and light colours, and shades)
- Fonts that are to thin
- Effects or designs that make it difficult to print
- Italic or old fashioned looking fonts, i.e. anything like Times New Roman is a NO!

```html
<!DOCTYPE html>
<html lang="en">
<head>
<meta charset="utf-8">
<title>Quill Harbor – Business Card</title>
<link href="https://fonts.googleapis.com/css2?family=Questrial&family=Noto+Serif:wght@400&family=Open+Sans:wght@400&display=swap" rel="stylesheet">
<style>
  :root {
    --bg: #eef0f1;
    --card-dark: #060807;
    --card-dark-sheen: #2f3131;
    --card-light: #ffffff;
    --teal: #1d93b0;
    --teal-deep: #0d8aa6;
    --teal-pale: #7fd0e2;
    --text-grey: #555b5e;
  }
  * { margin: 0; padding: 0; box-sizing: border-box; }
  html, body { width: 1200px; height: 900px; overflow: hidden; background: var(--bg); }
  .canvas {
    width: 1200px; height: 900px;
    display: flex; align-items: center; justify-content: center; gap: 40px;
  }
  .card {
    position: relative;
    width: 540px; height: 349px;
    border-radius: 26px;
    overflow: hidden;
    box-shadow: 0 10px 28px rgba(0,0,0,0.18);
  }
  /* Back side */
  .card--back {
    background: linear-gradient(152deg, var(--card-dark-sheen) 0%, var(--card-dark-sheen) 44%, var(--card-dark) 44.4%, var(--card-dark) 100%);
    display: flex; align-items: center; justify-content: center;
  }
  .brand-name {
    font-family: "Questrial", sans-serif;
    font-weight: 400;
    color: var(--teal);
    letter-spacing: -0.5px;
    line-height: 1;
  }
  .card--back .brand-name { font-size: 58px; }
  /* Front side */
  .card--front { background: var(--card-light); }
  .front-band {
    position: absolute; left: 0; right: 0; bottom: 0; height: 20px;
    background: var(--teal-deep);
  }
  .front-band__tip {
    position: absolute; right: 0; bottom: 0; width: 34px; height: 20px;
    background: var(--teal-pale);
  }
  .card--front .brand-name {
    position: absolute; left: 34px; bottom: 86px;
    font-size: 52px;
  }
  .contact-block {
    position: absolute; right: 40px; top: 44px;
    text-align: left;
  }
  .person-name {
    font-family: "Noto Serif", serif;
    font-size: 25px; color: var(--teal);
    line-height: 1.05;
  }
  .person-role {
    font-family: "Noto Serif", serif;
    font-size: 14px; color: var(--text-grey);
    margin-left: 52px;
  }
  .contact-list {
    list-style: none;
    margin-top: 58px;
    font-family: "Open Sans", sans-serif;
    font-size: 12.5px; color: var(--text-grey);
  }
  .contact-list li { display: flex; align-items: center; gap: 9px; margin-bottom: 12px; }
  .contact-list svg { width: 12px; height: 12px; flex: none; }
</style>
</head>
<body>
<main class="canvas">
  <section class="card card--back" aria-label="Card back">
    <span class="brand-name">Quill Harbor</span>
  </section>

  <section class="card card--front" aria-label="Card front">
    <span class="brand-name">Quill Harbor</span>

    <div class="contact-block">
      <p class="person-name">Edwin Marlow</p>
      <p class="person-role">Company Position</p>
      <ul class="contact-list">
        <li>
          <svg viewBox="0 0 12 12" aria-hidden="true"><rect x="0.75" y="2.25" width="10.5" height="7.5" fill="none" stroke="#1d93b0" stroke-width="1.5"/><path d="M1 3 L6 7 L11 3" fill="none" stroke="#1d93b0" stroke-width="1.3"/></svg>
          name@quillharbor.co.uk
        </li>
        <li>
          <svg viewBox="0 0 12 12" aria-hidden="true"><rect x="3" y="0.5" width="6" height="11" rx="1.2" fill="#1d93b0"/><rect x="4.2" y="2" width="3.6" height="6.5" fill="#ffffff"/></svg>
          +44 (0) 7700 900482
        </li>
      </ul>
    </div>

    <div class="front-band"><div class="front-band__tip"></div></div>
  </section>
</main>
</body>
</html>
```